The Deskwell (A new and exciting small Business support solution) Business Cards

The Deskwell Business Card Design

About us:
The Deskwell is a small business support solution, assisting businesses with any marketing, office management and human resource skills.

Objective
To be a small business lifesaver, to relieve busy professionals from mundane operations so they can focus on their businesses future through complete, reliable, efficient and effective client support. To have people say WOW what did we do before The Deskwell.

Industry/Entity Type

Small Business

Colors
0355a3
33a6d7

Requirements
Must have
• Must be similar to the look and feel of my website http://www.thedeskwell.com.au/

Must have:

Blue colour is 0094FF

The Logo

A Small Business Support Solution
- Human Resources
- Office Administration
- Marketing

Marisa Holt
0487 302 615
marisaholt@thedeskwell.com.au
www.thedeskwell.com

```html
<!DOCTYPE html>
<html lang="en">
<head>
<meta charset="utf-8">
<title>The Deskwell – Business Cards</title>
<link rel="stylesheet" href="https://fonts.googleapis.com/css2?family=Open+Sans:wght@400;600;700&family=Oswald:wght@500&display=swap">
<style>
  :root {
    --backdrop: #3b3131;
    --card: #ffffff;
    --brand-blue: #0094ff;
    --panel-blue: #5aa5e3;
    --ink: #111111;
    --body-ink: #2b2b2b;
    --on-blue: #ffffff;
  }
  * { margin: 0; padding: 0; box-sizing: border-box; }
  html, body {
    width: 1200px;
    height: 1000px;
    overflow: hidden;
    background: var(--backdrop);
  }
  .canvas {
    width: 1200px;
    height: 1000px;
    display: flex;
    flex-direction: column;
    align-items: center;
    justify-content: center;
    gap: 30px;
  }
  .card {
    position: relative;
    width: 820px;
    height: 455px;
    background: var(--card);
    overflow: hidden;
    box-shadow: 0 6px 18px rgba(0,0,0,0.35);
  }

  /* Front */
  .card--front .front-mark {
    position: absolute;
    left: 0;
    right: 0;
    top: 150px;
    text-align: center;
  }
  .wordmark {
    font-family: "Open Sans", sans-serif;
    font-weight: 400;
    color: var(--brand-blue);
    letter-spacing: -1px;
    line-height: 1;
  }
  .front-mark .wordmark { font-size: 96px; }
  .tagline {
    font-family: "Open Sans", sans-serif;
    font-weight: 400;
    color: var(--brand-blue);
    font-size: 24px;
    margin-top: 6px;
    padding-left: 120px;
  }

  /* Back */
  .card--back .back-mark {
    position: absolute;
    left: 56px;
    top: 92px;
  }
  .back-mark .wordmark { font-size: 36px; letter-spacing: 0; }

  .services {
    position: absolute;
    right: 0;
    top: 130px;
    width: 250px;
    height: 120px;
    background: var(--panel-blue);
    padding: 20px 0 0 34px;
    list-style: none;
    font-family: "Open Sans", sans-serif;
    font-size: 14px;
    line-height: 1.45;
    color: var(--on-blue);
  }

  .accent-block {
    position: absolute;
    left: 0;
    top: 322px;
    width: 78px;
    height: 96px;
    background: var(--panel-blue);
  }
  .contact {
    position: absolute;
    left: 112px;
    top: 318px;
  }
  .contact__name {
    font-family: "Oswald", sans-serif;
    font-weight: 500;
    font-size: 26px;
    color: var(--brand-blue);
    text-transform: uppercase;
    letter-spacing: 0.5px;
    line-height: 1.1;
    margin-bottom: 6px;
  }
  .contact__line {
    font-family: "Open Sans", sans-serif;
    font-weight: 700;
    font-size: 14px;
    color: var(--body-ink);
    line-height: 1.5;
    letter-spacing: 0.4px;
  }
</style>
</head>
<body>
<main class="canvas">
  <section class="card card--front" aria-label="Business card front">
    <div class="front-mark">
      <div class="wordmark">The Deskwell</div>
      <div class="tagline">A Small Business Support Solution</div>
    </div>
  </section>

  <section class="card card--back" aria-label="Business card back">
    <div class="back-mark">
      <div class="wordmark">The Deskwell</div>
    </div>

    <ul class="services">
      <li>Marketing Administration</li>
      <li>Office Management</li>
      <li>Human Resources</li>
      <li>Administration</li>
    </ul>

    <div class="accent-block"></div>
    <div class="contact">
      <p class="contact__name">Marisa Holt</p>
      <p class="contact__line">Phone : 0487 302 615</p>
      <p class="contact__line">Email : marisaholt@thedeskwell.com.au</p>
      <p class="contact__line">Website : www.thedeskwell.com.au</p>
    </div>
  </section>
</main>
</body>
</html>
```